Post card for Tax Preparation Services

Bramble Ledger, a accounting and tax solution firm is in need of a postcard to send to people who have moved into the area in the last year. The goal is to market our tax preparation services. More information on our business and services can be found on our website: www.brambleledger-example.com

Return address:
4817 Harrow Mill Pkwy
Bldg 300, Ste 410
Woodstock, GA 30274

Phone: (678) 555-7SUM

Please submit copies of front and back design in one submisstion. Do not submit duplicate designs.

Target Market(s)

People who have moved within 2 miles of our office

Industry/Entity Type

Accounting

Colors
6b449b
fbee3e

Requirements
Must have
• Logo
• Schedule Online
• Mention this postcard Receive $25.00 off tax prep
• Colors Gold #c6A734 and Purple #5f1547 to match logo
Should not have
• No cartoony feel

```html
<!DOCTYPE html>
<html lang="en">
<head>
<meta charset="utf-8">
<title>Bramble Ledger Postcard</title>
<link href="https://fonts.googleapis.com/css2?family=Josefin+Sans:wght@400;700&family=Roboto:wght@400;700&display=swap" rel="stylesheet">
<style>
  :root {
    --purple: #6b449b;
    --purple-light: #9a7cc4;
    --gold: #c6a734;
    --ink: #111111;
    --muted: #666666;
    --card: #f6f6f8;
    --page: #e4e2e6;
  }
  html, body {
    margin: 0;
    width: 1200px;
    height: 1200px;
    overflow: hidden;
    background: var(--page);
  }
  .postcard {
    position: absolute;
    left: 50px;
    top: 233px;
    width: 1100px;
    height: 734px;
    background: linear-gradient(135deg, #ffffff 0%, var(--card) 60%, #ececf0 100%);
    box-shadow: 0 10px 30px rgba(0,0,0,0.25);
    overflow: hidden;
    font-family: "Roboto", sans-serif;
    color: var(--ink);
  }
  .postcard-bands {
    position: absolute;
    inset: 0;
  }
  .brand {
    position: absolute;
    left: 80px;
    top: 140px;
    display: flex;
    align-items: center;
    gap: 18px;
  }
  .brand-mark {
    width: 54px;
    height: 54px;
    background: var(--gold);
  }
  .brand-name {
    font-family: "Josefin Sans", sans-serif;
    font-weight: 700;
    font-size: 66px;
    line-height: 1;
    color: var(--gold);
    letter-spacing: 1px;
  }
  .brand-tagline {
    font-family: "Josefin Sans", sans-serif;
    font-size: 26px;
    letter-spacing: 2px;
    color: var(--ink);
    margin-top: 4px;
  }
  .portrait {
    position: absolute;
    left: 110px;
    top: 290px;
    width: 320px;
    height: 330px;
    background: linear-gradient(135deg, #a0543a 0%, #b8633f 45%, #d9b08a 100%);
  }
  .services {
    position: absolute;
    left: 500px;
    top: 285px;
    margin: 0;
    padding: 0;
    list-style: none;
    font-size: 25px;
    line-height: 38px;
    text-transform: uppercase;
  }
  .services li {
    display: flex;
    align-items: center;
    gap: 14px;
  }
  .services svg { width: 24px; height: 24px; }
  .contact {
    position: absolute;
    left: 500px;
    top: 460px;
  }
  .contact-phone {
    font-weight: 700;
    font-size: 38px;
  }
  .contact-address {
    font-size: 18px;
    color: var(--muted);
    letter-spacing: 0.5px;
    margin-top: 6px;
  }
  .offer {
    position: absolute;
    left: 470px;
    top: 562px;
    font-size: 20px;
    line-height: 24px;
  }
</style>
</head>
<body>
  <div class="postcard">
    <svg class="postcard-bands" viewBox="0 0 1100 734" preserveAspectRatio="none" aria-hidden="true">
      <polygon points="0,40 1100,0 1100,120 0,50" fill="var(--purple)"/>
      <polygon points="640,30 1100,0 1100,250 960,40" fill="var(--purple-light)" opacity="0.55"/>
      <polygon points="800,40 1100,80 1100,200" fill="#ffffff" opacity="0.18"/>
      <polygon points="0,655 1100,615 1100,734 0,734" fill="var(--purple)"/>
    </svg>

    <div class="brand">
      <div class="brand-mark"></div>
      <div>
        <div class="brand-name">BRAMBLE LEDGER</div>
        <div class="brand-tagline">ACCOUNTING &amp; TAX SOLUTIONS</div>
      </div>
    </div>

    <div class="portrait" role="img" aria-label="Portrait photo of the firm's tax professional in front of a brick wall"></div>

    <ul class="services">
      <li><svg viewBox="0 0 24 24"><path d="M3 13l6 6L21 5" fill="none" stroke="#111" stroke-width="4"/></svg>Tax Preparation &amp; Planning</li>
      <li><svg viewBox="0 0 24 24"><path d="M3 13l6 6L21 5" fill="none" stroke="#111" stroke-width="4"/></svg>Accounting &amp; Bookkeeping</li>
      <li><svg viewBox="0 0 24 24"><path d="M3 13l6 6L21 5" fill="none" stroke="#111" stroke-width="4"/></svg>IRS Tax Resolution</li>
      <li><svg viewBox="0 0 24 24"><path d="M3 13l6 6L21 5" fill="none" stroke="#111" stroke-width="4"/></svg>Payroll Services</li>
    </ul>

    <div class="contact">
      <div class="contact-phone">Phone: (678) 555-7SUM</div>
      <div class="contact-address">4817 Harrow Mill Pkwy Bldg 300, Ste 410 Woodstock, GA 30274</div>
    </div>

    <div class="offer">Mention this postcard Receive $25.00 off tax prep</div>
  </div>
</body>
</html>
```